Vantor Health Group Presentation Folder, for Cancer Awareness, VERY COLORFUL AND MODERN

Presentation Folder I know pretty much what i want so it should be very eazy , I have included files from folders I use now rebrand them to my new company they will be fine, no sense re creating the wheel
Full Bleed Size
20.87" x 16.68"
53 x 42.4 cm
6260 x 5004 pixels
Document Trim Size
20.75" x 16.56"
52.7 x 42.1 cm
6225 x 4969 pixels
Updates

Low design quality

Industry/Entity Type

Medical

Font styles to use
Serif

Colors

Designer to choose colors to be used in the design.

Requirements
Must have
• really I am not looking for some one to redesign, we like our folder front page and would like to see new word information added., there are two folder front pages to choose from
• So Keep the original front page and redesign the back page and the pockets
• Can Make your Design off of one of the ones I already uploaded
Nice to have
• Keep the same color schemes, Keep the original front page and redesign the back page and the pockets
Should not have
• DO not recreate the front covers, use what I gave you and just rebrand

```html
<!DOCTYPE html>
<html lang="en">
<head>
<meta charset="utf-8">
<title>Vantor Health Group – Presentation Folder</title>
<link href="https://fonts.googleapis.com/css2?family=Raleway:wght@300;400;600;700&family=Arimo:wght@400;700&display=swap" rel="stylesheet">
<style>
  :root{
    --pink:#f394a7;
    --pink-deep:#c9466b;
    --grey:#6d6e71;
    --grey-box:#9d9c9f;
    --grey-strip:#d1d2d4;
    --navy:#1e2a5a;
    --white:#ffffff;
    --cut:#e2333a;
    --fold:#39b54a;
    --ink:#444;
  }
  html,body{margin:0;padding:0;overflow:hidden;background:#fff;}
  .folder{position:relative;width:1200px;height:960px;overflow:hidden;background:#fff;font-family:"Arimo",Arial,sans-serif;}
  .dieline{position:absolute;inset:0;pointer-events:none;}
  .abs{position:absolute;}

  /* back cover */
  .back{left:50px;top:64px;width:552px;height:633px;background:var(--pink);overflow:hidden;}
  .back-photo{left:0;top:0;width:552px;height:320px;
    background:
      linear-gradient(180deg,rgba(255,255,255,0) 0%,rgba(255,255,255,0) 62%,rgba(120,50,70,.35) 75%,rgba(90,35,55,.55) 100%),
      linear-gradient(180deg,#f7d3db 0%,#f0bccb 38%,#d896a8 52%,#c27a8f 62%,#b06a7f 100%);
    clip-path:polygon(0 0,100% 0,100% 274px,0 320px);}
  .quote-box{left:291px;top:244px;width:214px;height:205px;background:var(--grey-box);
    clip-path:polygon(0 0,100% 0,100% 180px,190px 100%,0 100%);}
  .quote-box .fold{position:absolute;right:0;bottom:0;width:26px;height:26px;background:#7a797c;clip-path:polygon(100% 0,100% 100%,0 100%);}
  .quote-box p{margin:0;padding:66px 18px 0 20px;font:600 15.5px/20px "Raleway",sans-serif;color:var(--white);}
  .back-headline{left:36px;top:362px;margin:0;font:700 29px/39px "Raleway",sans-serif;color:var(--white);}
  .back-body{left:36px;top:480px;width:469px;margin:0;font:400 9.2px/12px "Arimo",Arial,sans-serif;color:var(--white);text-align:justify;}
  .back-footer{left:0;top:572px;width:552px;height:61px;background:var(--grey);}
  .back-footer h2{position:absolute;left:304px;top:6px;margin:0;font:400 15.5px/20px "Raleway",sans-serif;color:var(--white);letter-spacing:.3px;}
  .back-footer .contact{position:absolute;left:304px;top:30px;margin:0;font:400 5.6px/9px "Arimo",Arial,sans-serif;color:var(--white);letter-spacing:.3px;}

  /* front cover */
  .front{left:602px;top:64px;width:552px;height:633px;background:var(--white);}
  .front-band{left:0;top:0;width:552px;height:45px;background:var(--pink);}
  .front-title{left:0;top:11px;width:552px;margin:0;text-align:center;font:300 21.5px/24px "Raleway",sans-serif;letter-spacing:3.4px;color:var(--white);}
  .front-sub{left:105px;top:45px;width:342px;height:36px;background:var(--grey-box);margin:0;font:600 11px/36px "Raleway",sans-serif;letter-spacing:.8px;color:var(--white);text-align:center;}
  .checklist{left:65px;top:110px;width:470px;margin:0;padding:0;list-style:none;display:grid;grid-template-columns:91px 87px 100px 73px 90px;row-gap:7px;}
  .checklist li{font:400 9.5px/12px "Raleway",sans-serif;color:var(--ink);display:flex;align-items:center;gap:3px;}
  .checklist svg{width:7px;height:7px;flex:none;}
  .front-photo{left:0;top:158px;width:552px;height:360px;
    background:
      linear-gradient(180deg,rgba(255,255,255,0) 0%,rgba(255,255,255,0) 48%,rgba(90,90,90,.25) 60%,rgba(70,70,70,.45) 100%),
      linear-gradient(100deg,#e9e9e9 0%,#bdbdbd 25%,#d8d8d8 50%,#a9a9a9 75%,#cfcfcf 100%);}
  .front-band-low{left:0;top:522px;width:552px;height:39px;background:var(--grey);}
  .front-band-low p{position:absolute;left:155px;top:8px;width:375px;margin:0;font:400 9.2px/12px "Arimo",Arial,sans-serif;color:var(--white);}
  .mark-dot{left:84px;top:552px;width:30px;height:30px;border-radius:50%;background:var(--white);border:1px solid #bbb;box-sizing:border-box;}
  .tagline{right:40px;top:570px;margin:0;font:300 11.5px/14px "Raleway",sans-serif;color:var(--ink);}
  .tagline b{font-weight:700;}

  /* pockets (printed upside down) */
  .pocket-copy{transform:rotate(180deg);}
  .left-copy{left:90px;top:697px;width:470px;height:258px;}
  .left-copy .division{position:absolute;left:66px;top:36px;width:335px;text-align:center;margin:0;}
  .left-copy .division .name{display:block;font:400 16px/20px "Raleway",sans-serif;color:var(--pink-deep);}
  .left-copy .division .sub{display:block;font:400 11px/16px "Raleway",sans-serif;color:var(--grey);margin-top:6px;}
  .brand{position:absolute;left:92px;top:100px;display:flex;align-items:center;gap:16px;}
  .brand .dot{width:76px;height:76px;border-radius:50%;background:var(--navy);flex:none;}
  .brand span{font:700 31px/33px "Raleway",sans-serif;color:var(--navy);letter-spacing:1px;width:170px;}
  .right-copy{left:645px;top:697px;width:470px;height:258px;}
  .right-copy h3{position:absolute;left:22px;top:24px;width:395px;margin:0;font:400 16px/20px "Raleway",sans-serif;color:var(--pink-deep);}
  .right-copy .col{position:absolute;margin:0;font:400 8.6px/11.4px "Arimo",Arial,sans-serif;color:var(--navy);text-align:justify;}
  .right-copy .col-a{left:22px;top:82px;width:200px;}
  .right-copy .col-b{left:249px;top:82px;width:200px;}
</style>
</head>
<body>
<div class="folder">

  <!-- pocket shapes -->
  <svg class="dieline" width="1200" height="960" viewBox="0 0 1200 960">
    <path d="M53 697 H600 L590 910 Q585 957 540 957 H53 Z" fill="var(--pink)"/>
    <rect x="53" y="697" width="37" height="260" fill="var(--grey-strip)"/>
    <path d="M606 697 H1152 V957 H690 Q648 957 645 912 Z" fill="var(--pink)"/>
    <rect x="1115" y="697" width="37" height="260" fill="var(--grey-strip)"/>
  </svg>

  <!-- back cover -->
  <section class="abs back">
    <div class="abs back-photo" role="img" aria-label="Photo of a family of three generations holding hands, seen from behind, facing the sea"></div>
    <div class="abs quote-box"><p>Knowledge is Power and Power Eradicates Fear. When You are Fearless, You Will Make all the Right Choices!</p><span class="fold"></span></div>
    <h1 class="abs back-headline">Don’t be Afraid<br>of the Answer.</h1>
    <p class="abs back-body">Hereditary cancer screening provides vital information to help people with a strong personal or family history of cancer understand their own risk of developing the disease. With this information, they can take steps to Potentially Prevent Cancer, Delay the Onset of Cancer or Catch it at an Earlier stage when outcomes and survival rates are Better.</p>
    <div class="abs back-footer">
      <h2>VANTOR HEALTH GROUP</h2>
      <p class="contact">2280 LARKMOOR AVENUE &nbsp;|&nbsp; SUITE B &nbsp;|&nbsp; BRENTON, GA 30499<br>(tel) 555.310.4821 &nbsp;|&nbsp; (fax) 555.310.4890 &nbsp;|&nbsp; care@vantorhealth.com</p>
    </div>
  </section>

  <!-- front cover -->
  <section class="abs front">
    <div class="abs front-band"></div>
    <h1 class="abs front-title">HEREDITARY CANCER SCREENING</h1>
    <p class="abs front-sub">Doctors are the Gatekeepers to Genetic Testing</p>
    <ul class="abs checklist">
      <li><svg viewBox="0 0 10 10"><rect x="0.5" y="0.5" width="9" height="9" fill="none" stroke="#999"/><path d="M2 5 L4.5 7.5 L9.5 1" fill="none" stroke="var(--pink-deep)" stroke-width="1.6"/></svg>BREASTR</li>
      <li><svg viewBox="0 0 10 10"><rect x="0.5" y="0.5" width="9" height="9" fill="none" stroke="#999"/><path d="M2 5 L4.5 7.5 L9.5 1" fill="none" stroke="var(--pink-deep)" stroke-width="1.6"/></svg>OVARIAN</li>
      <li><svg viewBox="0 0 10 10"><rect x="0.5" y="0.5" width="9" height="9" fill="none" stroke="#999"/><path d="M2 5 L4.5 7.5 L9.5 1" fill="none" stroke="var(--pink-deep)" stroke-width="1.6"/></svg>ENDOMETRIAL</li>
      <li><svg viewBox="0 0 10 10"><rect x="0.5" y="0.5" width="9" height="9" fill="none" stroke="#999"/><path d="M2 5 L4.5 7.5 L9.5 1" fill="none" stroke="var(--pink-deep)" stroke-width="1.6"/></svg>GASTRIC</li>
      <li><svg viewBox="0 0 10 10"><rect x="0.5" y="0.5" width="9" height="9" fill="none" stroke="#999"/><path d="M2 5 L4.5 7.5 L9.5 1" fill="none" stroke="var(--pink-deep)" stroke-width="1.6"/></svg>COLORECTAL</li>
      <li><svg viewBox="0 0 10 10"><rect x="0.5" y="0.5" width="9" height="9" fill="none" stroke="#999"/><path d="M2 5 L4.5 7.5 L9.5 1" fill="none" stroke="var(--pink-deep)" stroke-width="1.6"/></svg>PANCREATIC</li>
      <li><svg viewBox="0 0 10 10"><rect x="0.5" y="0.5" width="9" height="9" fill="none" stroke="#999"/><path d="M2 5 L4.5 7.5 L9.5 1" fill="none" stroke="var(--pink-deep)" stroke-width="1.6"/></svg>MELANOMA</li>
      <li><svg viewBox="0 0 10 10"><rect x="0.5" y="0.5" width="9" height="9" fill="none" stroke="#999"/><path d="M2 5 L4.5 7.5 L9.5 1" fill="none" stroke="var(--pink-deep)" stroke-width="1.6"/></svg>PROSTATE</li>
      <li><svg viewBox="0 0 10 10"><rect x="0.5" y="0.5" width="9" height="9" fill="none" stroke="#999"/><path d="M2 5 L4.5 7.5 L9.5 1" fill="none" stroke="var(--pink-deep)" stroke-width="1.6"/></svg>LUNG</li>
      <li><svg viewBox="0 0 10 10"><rect x="0.5" y="0.5" width="9" height="9" fill="none" stroke="#999"/><path d="M2 5 L4.5 7.5 L9.5 1" fill="none" stroke="var(--pink-deep)" stroke-width="1.6"/></svg>COLON</li>
    </ul>
    <div class="abs front-photo" role="img" aria-label="Black and white photo of a multi-generation family sharing a meal at an outdoor table"></div>
    <div class="abs front-band-low"><p>We have an obligation to help patients understand genetic risk and how testing can guide heath care decisions.</p></div>
    <div class="abs mark-dot"></div>
    <p class="abs tagline">The test you order <b>FOR</b> your patients</p>
  </section>

  <!-- left pocket -->
  <div class="abs pocket-copy left-copy">
    <p class="division"><span class="name">Vantor Health Group</span><span class="sub">a division of Meridian Clinical Sales LLC</span></p>
    <div class="brand"><span class="dot"></span><span>VANTOR HEALTH GROUP</span></div>
  </div>

  <!-- right pocket -->
  <div class="abs pocket-copy right-copy">
    <h3>Identifying an inherited genetic mutation has the potential to prevent cancer and save lives.</h3>
    <p class="col col-a">There are many benefits to getting tested, regardless of the eventual result. If one of your family members — however distant — had cancer, there is a chance that you inherited a gene mutation that not only increases your personal risk of cancer, but also could be passed to the next generation. Those who are carriers of hereditary cancer gene mutations, could be at risk of getting cancer earlier in life than the general population. The sooner genetic testing is done, the more likely it is that the risk can be managed appropriately.</p>
    <p class="col col-b">Hereditary cancer screening provides vital information to help people with a strong personal or family history of cancer understand their own risk of developing the disease. With this information, they can take steps to Potentially Prevent Cancer, Delay the Onset of Cancer or Catch it at an Earlier stage when outcomes and survival rates are Better.</p>
  </div>

  <!-- cut and fold lines -->
  <svg class="dieline" width="1200" height="960" viewBox="0 0 1200 960">
    <g fill="none" stroke="var(--cut)" stroke-width="1">
      <path d="M50 697 V64 M50 6 H1154 M1154 64 V697"/>
      <path d="M50 6 V20 L8 20 V420 A20 20 0 0 1 8 460 V688 L50 697"/>
      <path d="M1154 6 V20 L1196 20 V420 A20 20 0 0 0 1196 460 V688 L1154 697"/>
      <path d="M53 697 V957 H540 Q585 957 590 910 L600 697"/>
      <path d="M606 697 L645 912 Q648 957 690 957 H1152 V697"/>
    </g>
    <g fill="none" stroke="var(--fold)" stroke-width="0.8" stroke-dasharray="3 3">
      <path d="M50 6 V64 M602 6 V697 M1154 6 V64 M50 697 H1154"/>
    </g>
  </svg>
</div>
</body>
</html>
```